BlinkoNovaFizz Home Page and Visual Style Specification

I've already gota home page, but I'm not totally happy with it. I've included a mockup of what i have so you have a starting point. I don't thing the logo looks good in the header - the colors seems off. I like the gradient background - just wondering if you can come up with a better design overall.

1. Project goal
Capture email leads, promote BlinkoNovaFizz products and courses, and reinforce Blinko brand vibe that is playful and trustworthy.

2. Brand assets provided
* Logo text graphic BlinkoNovaFizzLogo.png
* Planet emblem artwork BlinkoNovaFizzHighResIconPic.jpg
Minor tweaks to the logo are allowed if they improve clarity at small sizes.

3. Core color palette
* Hot pink #FF2D95
* Vivid purple #9E38FF
* Electric blue #00A3FF
* Cosmic gold #EADFA3
Background uses a diagonal gradient from hot pink at top left through vivid purple in the center to electric blue at bottom right.
Apply a subtle white overlay at ten percent opacity across the gradient for text readability.

4. Typography
* Headings Google Audiowide, letter spacing two percent, bold weight
* Body Roboto regular, line height one point six
* Fallback stack "Audiowide", "Roboto", Arial, sans serif

5. Layout and spacing
* Content width on desktop maximum twelve hundred pixels, centered
* Base spacing unit eight pixels, scaled by multiples for harmony
* Twelve column grid on desktop, four column grid on tablet, single column flow on mobile

6. Navigation bar
* Logo centered in the bar
* Left links Courses, My Charts, PomroTalk
* Right links About, Contact, Blog
* Far right button LOGIN styled as primary action
* Navigation bar remains visible while scrolling

7. Hero section
* Full viewport height on desktop, seventy percent viewport height on mobile
* Left half shows planet emblem artwork with soft glow
* Right half contains headline in Audiowide, subhead in Roboto, and email opt in form with single field and Board the Orbit Roll button
* Button uses cosmic gold background and hot pink hover glow

8. Section order after hero
1. Products carousel with swipe support on mobile and four cards visible on desktop
2. Featured courses presented in a zigzag layout with course cover images and View course buttons
3. Latest blog posts in a three card grid with thumbnail, title, and read time
4. About Blinko section with portrait illustration, short origin story paragraph, and Read more link
5. Contact form with name, email, message, and captcha
6. Secondary opt in banner with same form as hero

9. Imagery and iconography
* Use cosmic vibrant stock images with real star fields or stylized nebulae
* Apply outlined icons with slight inner glow that matches the neon palette
* Provide descriptive alt text for all images

10. Accessibility essentials
* Maintain contrast ratio of at least four point five to one between text and background
* Ensure keyboard focus order follows visual flow
* Provide aria labels for navigation, forms, and carousel controls

11. Responsive behavior priorities
* Design mobile first because seventy five percent of traffic is mobile
* Below seven hundred sixty pixels collapse navigation links into a full width drawer activated by a hamburger icon
* Carousel uses swipe gestures on touch devices
* Hero artwork scales down and stacks above text on narrow screens

12. Deliverables
* Layered PSD file with clear group naming for every section, typography styles, and color swatches
* Printable PDF style guide that summarizes palette, fonts, logo usage, and component spacing

```html
<!DOCTYPE html>
<html lang="en">
<head>
<meta charset="utf-8">
<title>BlinkoNovaFizz — Home</title>
<link rel="stylesheet" href="https://fonts.googleapis.com/css2?family=Audiowide&family=Montserrat:wght@400;500;600;700&family=Roboto:wght@400;500;700&display=swap">
<style>
:root{
  --pink:#ff0a8c;
  --purple:#9e28ff;
  --blue:#1a8fff;
  --gold:#eadfa3;
  --gold-text:#f6e8a6;
  --btn-text:#e3245c;
  --card:rgba(255,255,255,0.16);
  --field-border:#27e0c8;
  --neon-green:#39ff14;
  --white:#ffffff;
}
*{box-sizing:border-box;margin:0;padding:0}
html,body{width:1200px;height:5004px;overflow:hidden}
body{
  position:relative;
  font-family:"Montserrat",Arial,sans-serif;
  color:var(--white);
  background:linear-gradient(158deg,var(--pink) 0%,var(--pink) 16%,var(--purple) 38%,var(--blue) 60%,var(--blue) 100%);
}
a{text-decoration:none;color:inherit}
.abs{position:absolute}
.heading{
  font-family:"Audiowide",sans-serif;
  font-weight:400;
  color:var(--gold-text);
  letter-spacing:.02em;
  text-shadow:0 0 10px rgba(255,240,170,.75);
  text-align:center;
  width:1200px;left:0;
  font-size:36px;
}
.btn{
  position:absolute;display:flex;align-items:center;justify-content:center;
  background:var(--gold);color:var(--btn-text);
  font:700 13px "Montserrat",sans-serif;text-transform:uppercase;letter-spacing:.03em;
  border-radius:7px;border:2px solid #f8efc4;
  box-shadow:0 0 8px rgba(255,240,170,.6);
  white-space:nowrap;
}
/* nav */
.nav-link{position:absolute;top:32px;font:500 13px "Montserrat",sans-serif;color:var(--white);transform:translateX(-50%);white-space:nowrap}
.brand{position:absolute;font-family:"Audiowide",sans-serif;font-weight:400;color:var(--gold-text);white-space:nowrap}
/* hero */
.hero{left:120px;top:82px;width:958px;height:477px;background:var(--card);border-radius:8px}
.hero-art{left:124px;top:85px;width:468px;height:468px;border-radius:8px;
  background:radial-gradient(circle at 55% 40%,#c15cff 0%,#7a1fb0 35%,#2a0a45 75%,#1a0630 100%);
  box-shadow:0 0 24px rgba(255,110,220,.6)}
.hero-title{left:623px;top:140px;font-family:"Audiowide",sans-serif;font-weight:400;font-size:44px;line-height:55px;color:var(--gold-text);letter-spacing:.02em;white-space:nowrap}
.hero-sub{left:623px;top:318px;width:400px;font:400 14.5px/27px "Roboto",sans-serif}
.input{position:absolute;border:2px solid #ffd2e6;border-radius:8px;color:#ffe3ef;font:400 13px "Montserrat",sans-serif;padding-left:16px;display:flex;align-items:center;background:rgba(255,255,255,.06);white-space:nowrap}
/* products */
.product{top:699px;width:230px;height:435px;background:var(--card);border-radius:6px;text-align:center}
.product .thumb{height:183px;border-radius:6px 6px 0 0}
.product h3{margin-top:28px;font:500 17px "Roboto",sans-serif;color:var(--gold-text);white-space:nowrap}
.product p{margin:12px auto 0;width:200px;font:400 12.5px/24px "Montserrat",sans-serif;height:72px}
.product .price{margin-top:16px;font:500 25px "Roboto",sans-serif;color:var(--gold-text)}
.product .btn{left:48px;top:366px;width:134px;height:46px}
.arrow{position:absolute;top:906px;width:32px;height:32px}
/* courses */
.course-img{border-radius:4px}
.course-box{background:var(--card);border-radius:4px;padding:54px 30px 0 34px}
.course-box h3{font:500 16.5px "Roboto",sans-serif;color:var(--gold-text);white-space:nowrap}
.course-box p{margin-top:14px;font:400 13px/27px "Montserrat",sans-serif;width:310px}
.course-box .btn{position:relative;margin-top:20px;width:134px;height:44px}
/* blog */
.blog-band{left:0;top:3177px;width:1200px;height:699px;background:rgba(255,255,255,.1)}
.post{top:3317px;width:291px;height:404px;background:var(--card);border-radius:4px}
.post .thumb{height:210px;border-radius:4px 4px 0 0}
.post .date{position:absolute;left:16px;top:190px;width:106px;height:31px;background:var(--neon-green);color:#0b2a00;font:700 13px "Montserrat",sans-serif;display:flex;align-items:center;justify-content:center}
.post h3{position:absolute;left:16px;top:247px;width:260px;font:600 19px/29px "Montserrat",sans-serif}
.post .rule{position:absolute;left:16px;top:308px;width:78px;height:3px;background:var(--neon-green)}
.post p{position:absolute;left:20px;top:330px;width:255px;font:400 12.5px/25px "Montserrat",sans-serif}
/* contact */
.contact{left:118px;top:4204px;width:960px;height:461px;background:rgba(255,255,255,.14);border-radius:8px}
.field{position:absolute;border:2px solid var(--field-border);border-radius:8px;font:400 13px "Montserrat",sans-serif;padding:16px 18px;background:rgba(255,255,255,.05)}
.captcha{left:179px;top:4517px;width:283px;height:66px;background:#f9f9f9;border:1px solid #d3d3d3;border-radius:4px;color:#222;font:400 12.5px "Roboto",sans-serif}
.social{position:absolute;top:4834px;width:35px;height:35px;border-radius:50%;border:2px solid var(--gold);box-shadow:0 0 6px rgba(255,240,170,.6)}
</style>
</head>
<body>

<!-- navigation -->
<nav aria-label="Main navigation">
  <a class="nav-link" style="left:184px">Courses</a>
  <a class="nav-link" style="left:272px">My Charts</a>
  <a class="nav-link" style="left:365px">PomroTalk</a>
  <div class="brand" style="left:598px;top:24px;transform:translateX(-50%);font-size:24px">BlinkoNovaFizz</div>
  <a class="nav-link" style="left:777px">About</a>
  <a class="nav-link" style="left:849px">Contact</a>
  <a class="nav-link" style="left:917px">Blog</a>
  <a class="btn" style="left:961px;top:19px;width:113px;height:43px">Login</a>
</nav>

<!-- hero -->
<section aria-label="Hero">
  <div class="abs hero"></div>
  <div class="abs hero-art" role="img" aria-label="Planet emblem artwork: ringed planet among pink clouds"></div>
  <h1 class="abs hero-title">Aligned skin<br>begins with<br>intention.</h1>
  <p class="abs hero-sub">Get stellar updates, discounts, and exclusive astrology insights from Blinko.</p>
  <div class="input" style="left:623px;top:394px;width:206px;height:45px">Enter Your Email Address</div>
  <a class="btn" style="left:841px;top:394px;width:200px;height:45px">Board the Orbit Roll</a>
</section>

<!-- products -->
<h2 class="abs heading" style="top:630px">OUR PRODUCTS</h2>
<svg class="arrow" style="left:38px" viewBox="0 0 32 32" aria-label="Previous products"><circle cx="16" cy="16" r="14" fill="none" stroke="#fff" stroke-width="2"/><path d="M22 16H10M15 11l-5 5 5 5" fill="none" stroke="#fff" stroke-width="2"/></svg>
<svg class="arrow" style="left:1126px" viewBox="0 0 32 32" aria-label="Next products"><circle cx="16" cy="16" r="14" fill="none" stroke="#fff" stroke-width="2"/><path d="M10 16h12M17 11l5 5-5 5" fill="none" stroke="#fff" stroke-width="2"/></svg>

<div class="abs product" style="left:116px">
  <div class="thumb" role="img" aria-label="Glowing blue crystal mountain under a full moon" style="background:linear-gradient(180deg,#020a2a,#0a3f9c 55%,#29c6ff 80%,#06236b)"></div>
  <h3>Moon Vibes Crystal Kit</h3>
  <p>Align with lunar energy using hand-picked crystals charged under the full moon.</p>
  <div class="price">$28.00</div>
  <a class="btn">Shop Now</a>
</div>
<div class="abs product" style="left:359px">
  <div class="thumb" role="img" aria-label="Spiral galaxy with golden rings" style="background:radial-gradient(ellipse at 50% 55%,#f3c27a,#8a4a2a 35%,#2a1f3a 70%,#0c0c1c)"></div>
  <h3>NovaFizz Aura Spray</h3>
  <p>A mystical blend of botanicals to cleanse your vibe and boost your alignment.</p>
  <div class="price">$22.00</div>
  <a class="btn">Shop Now</a>
</div>
<div class="abs product" style="left:602px">
  <div class="thumb" role="img" aria-label="Planets over a pink and blue nebula" style="background:linear-gradient(160deg,#0b0f33,#3a1a5c 50%,#b03a8a 70%,#141436)"></div>
  <h3>Zodiac Sticker Pack</h3>
  <p>12 vibrant signs, reimagined as cosmic cuties — perfect for laptops, journals &amp; gifts.</p>
  <div class="price">$28.00</div>
  <a class="btn">Shop Now</a>
</div>
<div class="abs product" style="left:845px">
  <div class="thumb" role="img" aria-label="Golden planets lined up in dark space" style="background:linear-gradient(135deg,#2b1a0a,#8a5a1c 35%,#1a1208 70%,#0a0806)"></div>
  <h3>Birth Chart Decoder</h3>
  <p>A printable scroll of your natal chart explained in Blinko style — fun + empowering.</p>
  <div class="price">$28.00</div>
  <a class="btn">Shop Now</a>
</div>

<!-- featured courses -->
<h2 class="abs heading" style="top:1207px">FEATURED COURSES</h2>

<div class="abs course-img" style="left:136px;top:1297px;width:513px;height:396px;background:radial-gradient(ellipse at 62% 60%,#f0c58a,#8a5a4a 25%,#2a2a40 60%,#15182a)" role="img" aria-label="Galaxy with golden astrological chart lines"></div>
<div class="abs course-box" style="left:649px;top:1350px;width:390px;height:289px;padding-left:24px">
  <h3>Chart Whisperer 101</h3>
  <p>Learn how to interpret the planets, signs, and houses in your natal chart—without boring astro-jargon. This course breaks it down with clarity, memes, and a sprinkle of moon dust.</p>
  <a class="btn">View Course</a>
</div>

<div class="abs course-box" style="left:142px;top:1781px;width:415px;height:291px">
  <h3>Lunar Flow Masterclass</h3>
  <p>Learn how to interpret the planets, signs, and houses in your natal chart—without boring astro-jargon. This course breaks it down with clarity, memes, and a sprinkle of moon dust.</p>
  <a class="btn">View Course</a>
</div>
<div class="abs course-img" style="left:557px;top:1728px;width:513px;height:397px;background:linear-gradient(180deg,#0d1a30,#2a4260 45%,#6a8aa8 60%,#14263e)" role="img" aria-label="Moon phases above clouds"></div>

<div class="abs course-img" style="left:132px;top:2160px;width:515px;height:396px;background:linear-gradient(90deg,#c02a4a,#1a1a4a 35%,#10123a 65%,#2a8ad0)" role="img" aria-label="Two dragons facing each other in space"></div>
<div class="abs course-box" style="left:647px;top:2213px;width:390px;height:291px;padding-left:24px">
  <h3>AstroLove: Synastry &amp; Soulmates</h3>
  <p>Learn how to interpret the planets, signs, and houses in your natal chart—without boring astro-jargon. This course breaks it down with clarity, memes, and a sprinkle of moon dust.</p>
  <a class="btn">View Course</a>
</div>

<div class="abs course-box" style="left:140px;top:2645px;width:415px;height:291px">
  <h3>Planetary Retrogrades Demystified</h3>
  <p>Learn how to interpret the planets, signs, and houses in your natal chart—without boring astro-jargon. This course breaks it down with clarity, memes, and a sprinkle of moon dust.</p>
  <a class="btn">View Course</a>
</div>
<div class="abs course-img" style="left:553px;top:2593px;width:515px;height:396px;background:radial-gradient(circle at 50% 42%,#bfe6ff,#3a7ae0 20%,#1a3290 45%,#0a1240 80%)" role="img" aria-label="Blue spiral galaxy over mountains"></div>

<a class="btn" style="left:526px;top:3043px;width:134px;height:45px">View All</a>

<!-- latest blog -->
<section class="abs blog-band" aria-label="Latest blog"></section>
<h2 class="abs heading" style="top:3244px">LASTEST BLOG</h2>
<article class="abs post" style="left:130px">
  <div class="thumb" role="img" aria-label="Orange and blue nebula" style="background:radial-gradient(ellipse at 45% 50%,#ffb07a,#c0406a 30%,#2a2a6a 65%,#0a0c22)"></div>
  <div class="date">16 JUL 2025</div>
  <h3>Lorem Ipsum is simply dummy text printing</h3>
  <div class="rule"></div>
  <p>Lorem Ipsum is simply dummy text of the printing and typesetting</p>
</article>
<article class="abs post" style="left:452px">
  <div class="thumb" role="img" aria-label="Golden spiral galaxy" style="background:radial-gradient(circle at 50% 50%,#fff0b0,#f0a030 25%,#8a3a10 50%,#1a0c10)"></div>
  <div class="date">16 JUL 2025</div>
  <h3>Lorem Ipsum is simply dummy text printing</h3>
  <div class="rule"></div>
  <p>Lorem Ipsum is simply dummy text of the printing and typesetting</p>
</article>
<article class="abs post" style="left:775px">
  <div class="thumb" role="img" aria-label="Purple and blue swirling nebula" style="background:radial-gradient(circle at 50% 50%,#e080ff,#7a30d0 25%,#2a1a80 50%,#06061a)"></div>
  <div class="date">16 JUL 2025</div>
  <h3>Lorem Ipsum is simply dummy text printing</h3>
  <div class="rule"></div>
  <p>Lorem Ipsum is simply dummy text of the printing and typesetting</p>
</article>
<a class="btn" style="left:532px;top:3756px;width:134px;height:43px">View All</a>

<!-- about -->
<section aria-label="About Blinko">
  <h2 class="abs heading" style="top:3951px">ABOUT BLINKO</h2>
  <p class="abs" style="left:220px;top:4019px;width:760px;text-align:center;font:400 13.5px/28px 'Montserrat',sans-serif">Born from moonlight and memes, Blinko's mission is to bring stellar alignment to earthlings everywhere. A certified chart whisperer, Blinko has helped thousands tune in to their cosmic selves.</p>
  <a class="btn" style="left:532px;top:4092px;width:134px;height:42px">Read More</a>
</section>

<!-- contact -->
<section aria-label="Contact form">
  <div class="abs contact"></div>
  <h2 class="abs heading" style="top:4256px">CONTACT US</h2>
  <div class="field" style="left:177px;top:4329px;width:272px;height:49px">Name</div>
  <div class="field" style="left:460px;top:4329px;width:272px;height:49px">Email Address</div>
  <div class="field" style="left:746px;top:4329px;width:274px;height:49px">Phone Nmber</div>
  <div class="field" style="left:177px;top:4393px;width:843px;height:109px">Message</div>
  <div class="abs captcha">
    <div class="abs" style="left:14px;top:21px;width:24px;height:24px;border:2px solid #c1c1c1;border-radius:2px;background:#fff"></div>
    <div class="abs" style="left:52px;top:26px">I'm not a robot</div>
    <div class="abs" style="left:226px;top:10px;width:24px;height:24px;background:#4a90e2;border-radius:3px"></div>
    <div class="abs" style="left:206px;top:38px;font-size:9px;color:#555;text-align:center;width:64px">HumanCheck<br>Privacy · Terms</div>
  </div>
  <a class="btn" style="left:903px;top:4525px;width:113px;height:43px">Submit</a>
</section>

<!-- secondary opt-in -->
<section aria-label="Subscribe">
  <h2 class="abs" style="left:132px;top:4732px;font-family:'Audiowide',sans-serif;font-weight:400;font-size:21px;color:var(--gold-text);letter-spacing:.02em;text-shadow:0 0 8px rgba(255,240,170,.7);white-space:nowrap">SUBSCRIBE TO OUR COSMIC LIST</h2>
  <div class="input" style="left:132px;top:4787px;width:408px;height:47px;border-color:var(--field-border);box-shadow:0 0 8px rgba(39,224,200,.5)">Enter Your Email Address</div>
  <a class="btn" style="left:134px;top:4849px;width:198px;height:45px">Board the Orbit Roll</a>
  <div class="brand" style="left:629px;top:4744px;font-size:34px">BlinkoNovaFizz</div>
  <span class="social" style="left:630px" aria-label="Social profile 1"></span>
  <span class="social" style="left:686px" aria-label="Social profile 2"></span>
  <span class="social" style="left:740px" aria-label="Social profile 3"></span>
</section>

<!-- footer -->
<footer>
  <div class="abs" style="left:118px;top:4939px;width:960px;height:2px;background:var(--field-border)"></div>
  <p class="abs" style="left:0;top:4964px;width:1200px;text-align:center;font:400 12.5px 'Montserrat',sans-serif">© 2025 BlinkoNovaFizz | All Rights Reserved</p>
</footer>

</body>
</html>
```